New Packaging Design for Olives

We are looking for a new packaging design for our product.
- Clear plastic cup container
- 90mm round lid and tapers down to 45mm base
- We do not want a box
- We would like a cardboard wrap around.
Product:
- Pitted Kalamata Olives
- 90g Net
We would like to product to be displayed from top view and side view.
We would like an image of kalamata olives on the packaging
our logo to appear on top and side
the bottom of the packaging to have room for a bar code, ingredients & nutritional panel.
This product is designed to target the accommodation/hotel market and we are wanting a classy looking design to attract mini bar customers.
Attached is an image of the cup & an internal mock up and our company logo.
We need a design that will seamlessly work across a variety of products including salsa, chilli sauce, tomato sauce and others.
Target Market(s)
Hotel Mini bar at 4 to 5 star hotels
Industry/Entity Type
Hotel
Look and feel

```html
<!DOCTYPE html>
<html lang="en">
<head>
<meta charset="utf-8">
<title>Hartwell Pitted Kalamata Olives – Wrap Design</title>
<link href="https://fonts.googleapis.com/css2?family=Pacifico&family=Montserrat:wght@400;600&display=swap" rel="stylesheet">
<style>
  :root {
    --bg: #e9e9e7;
    --wrap-white: #ffffff;
    --side-white: #f4f4f4;
    --olive-red: #b0535a;
    --olive-deep: #7a2430;
    --olive-light: #c9707a;
    --maroon: #7a2f33;
    --leaf-green: #52b33c;
    --leaf-dark: #2f8a25;
    --ink: #333333;
  }
  * { box-sizing: border-box; margin: 0; padding: 0; }
  html, body { width: 1200px; height: 800px; overflow: hidden; background: var(--bg); }
  .canvas {
    position: relative; width: 1200px; height: 800px;
    display: flex; align-items: center; justify-content: center; gap: 60px;
    font-family: "Montserrat", Arial, sans-serif;
  }
  .panel {
    position: relative;
    box-shadow: 0 8px 24px rgba(0,0,0,.12);
  }
  /* Top (lid) panel */
  .panel-top {
    width: 520px; height: 520px; background: var(--wrap-white);
  }
  .single-serve {
    position: absolute; left: 22px; top: 34px;
    width: 170px; height: 34px;
  }
  .single-serve text {
    font-family: "Montserrat", Arial, sans-serif; font-size: 15px; fill: #fff;
  }
  .olive-image {
    position: absolute; left: 120px; top: 70px; width: 370px; height: 150px;
    border-radius: 50%;
    background: radial-gradient(ellipse at 45% 40%, var(--olive-light) 0%, var(--olive-red) 45%, var(--olive-deep) 100%);
  }
  .product-title {
    position: absolute; left: 70px; top: 270px;
    transform: rotate(-12deg); transform-origin: left top;
    color: var(--olive-red);
    font-family: "Pacifico", cursive;
    font-weight: 400;
    line-height: 1;
  }
  .product-title .pitted { display: block; font-size: 26px; margin-left: 70px; }
  .product-title .name { display: block; font-size: 52px; }
  .product-title .variety { display: block; font-size: 56px; margin-left: 150px; }
  .product-title .claim {
    display: block; margin-left: 190px; margin-top: 4px;
    font-family: "Montserrat", Arial, sans-serif; font-weight: 400; font-size: 18px; color: var(--ink);
  }
  .net-weight {
    position: absolute; right: 8px; top: 210px;
    writing-mode: vertical-rl;
    font-size: 12px; font-weight: 600; color: var(--ink); letter-spacing: .5px;
  }
  /* Side panel */
  .panel-side {
    width: 520px; height: 300px; background: var(--side-white);
    border-left: 18px solid var(--maroon);
    border-right: 18px solid var(--maroon);
  }
  .brand {
    position: absolute; left: 50%; top: 50%; transform: translate(-50%, -50%);
  }
  .brand-name {
    font-family: "Montserrat", Arial, sans-serif; font-weight: 600;
    font-size: 52px; color: var(--olive-red); line-height: 1;
  }
</style>
</head>
<body>
<main class="canvas">
  <section class="panel panel-top" aria-label="Lid panel">
    <svg class="single-serve" viewBox="0 0 170 34" aria-label="Single Serve">
      <polygon points="0,34 8,8 170,0 162,26" fill="var(--leaf-green)"/>
      <polygon points="0,34 8,8 0,14" fill="var(--leaf-dark)"/>
      <text x="26" y="24" transform="rotate(-4 85 17)">Single Serve</text>
    </svg>
    <div class="olive-image" role="img" aria-label="Photograph of glossy pitted kalamata olives"></div>
    <h1 class="product-title">
      <span class="pitted">Pitted</span>
      <span class="name">Kalamata</span>
      <span class="variety">Olives</span>
      <span class="claim">100% Natural</span>
    </h1>
    <p class="net-weight">90g NET</p>
  </section>

  <section class="panel panel-side" aria-label="Side panel">
    <div class="brand">
      <span class="brand-name">Hartwell</span>
    </div>
  </section>
</main>
</body>
</html>
```